Exclusive Wine Label for Australia

We require a new and exclusive wine label for one of our key clients. We are a family winery based in Western Australia with a premium focus. The wine will mainly be sold online so the label will require visual appeal and and a premium focus to fit a price point between $25-$30.

The label will be a revamp of an existing label of ours called Tallow Ridge (bottle image attached) . The only criteria required is to use the name. It can have a totally new look and theme to it. When investigating concepts, look at what the region, Margaret River is know for. It's all about the coastal environment, natural appeal and the relaxed lifestyle that people enjoy when visiting.

The label should be vibrant, colorful and not too serious.

I've also attached one of our labels Tre Colline. This is to give you the structure and layout of how we want the label (please ignore the graphic design and the use of our brand Velmonte) . It's a single wrap label with the dimensions of 88mm tall x 170mm wide.

Our preference is to not use too many expensive finishes such as foils, but embossing and high builds are fine. Velmonte logo is not required and our winery will only be displayed in text where it shows where the product is made.

Target Market(s)

30-50 yrs. No specific gender, but more towards a feminine look

Requirements
Must have
• - Follow the layout of the Tre Colline Label attached.
- Tallow Ridge as the Brand name on label. No reference to Velmonte required
- Fit the price point of $25-30
Nice to have
• It can have a retro look or it can be minimal and modern. I won't put examples up as we are looking for new concepts. Beach themed is the best approach and open to using people on the label as well. Otherwise you can explore making the text as the feature.
Should not have
• Swirls and Waves are overdone. Looking for something more creative.

```html
<!DOCTYPE html>
<html lang="en">
<head>
<meta charset="utf-8">
<title>Tallow Ridge – Cabernet Merlot Labels</title>
<link rel="stylesheet" href="https://fonts.googleapis.com/css2?family=EB+Garamond:wght@400;500&family=IM+Fell+English:ital@1&family=Josefin+Sans:wght@300&family=Great+Vibes&display=swap">
<style>
  :root {
    --frame: #7b0a6f;
    --paper: #f0f6fa;
    --ink: #3f2c3d;
    --accent: #7a2d5e;
    --shell: #7c3060;
    --shell-soft: #9a4a7a;
  }
  * { box-sizing: border-box; margin: 0; padding: 0; }
  html, body { width: 960px; height: 1200px; overflow: hidden; background: var(--frame); }
  .sheet { position: relative; width: 960px; height: 1200px; }
  .label {
    position: absolute; left: 0; width: 960px; height: 600px;
    background: var(--paper);
    border: 5px solid var(--frame);
    overflow: hidden;
  }
  .label--top { top: 0; }
  .label--bottom { top: 600px; border-top-width: 3px; }

  .shell-art {
    position: absolute;
    background: radial-gradient(ellipse at 40% 35%, var(--shell) 0%, var(--shell-soft) 70%, rgba(154,74,122,0.55) 100%);
  }
  .shell-art--conch { left: 381px; top: 64px; width: 206px; height: 194px; border-radius: 48% 52% 46% 54% / 40% 50% 50% 60%; }
  .shell-art--cockle { left: 350px; top: 76px; width: 252px; height: 186px; border-radius: 60% 55% 50% 50% / 55% 60% 45% 45%; }

  .est {
    position: absolute; top: 150px;
    font-family: "EB Garamond", serif; font-size: 20px; color: var(--ink);
    letter-spacing: 6px; font-variant-numeric: oldstyle-nums;
  }
  .est--word { left: 252px; }
  .est--year { left: 650px; }

  .brand {
    position: absolute; left: 0; right: 0; top: 300px;
    text-align: center;
    font-family: "IM Fell English", serif; font-style: italic;
    font-size: 86px; line-height: 1; color: var(--ink);
  }
  .region {
    position: absolute; left: 0; right: 0; top: 412px;
    text-align: center;
    font-family: "Josefin Sans", sans-serif; font-weight: 300;
    font-size: 24px; letter-spacing: 7px; color: var(--ink);
  }
  .varietal {
    position: absolute; left: 0; right: 0; top: 530px;
    text-align: center;
    font-family: "Great Vibes", cursive; font-size: 44px; line-height: 1; color: var(--ink);
  }

  .side {
    position: absolute; text-align: center; color: var(--accent);
    font-family: "EB Garamond", serif; font-variant-numeric: oldstyle-nums;
    white-space: nowrap;
  }
  .side--left { transform: translate(-50%, -50%) rotate(-90deg); }
  .side--right { transform: translate(-50%, -50%) rotate(90deg); }
  .side-heading { font-size: 14px; letter-spacing: 2.5px; }
  .side-copy { font-size: 9.4px; line-height: 15.5px; letter-spacing: 0.4px; width: 540px; white-space: normal; }

  .origin { left: 38px; top: 322px; }
  .notes-left { left: 82px; top: 318px; }
  .bottling { left: 913px; top: 308px; font-size: 15px; }
  .notes-right { left: 874px; top: 306px; }
</style>
</head>
<body>
<main class="sheet">

  <section class="label label--top">
    <div class="shell-art shell-art--conch" role="img" aria-label="Engraved illustration of a conch seashell in plum ink"></div>
    <span class="est est--word">EST.</span>
    <span class="est est--year">1920</span>
    <h1 class="brand">Tallow Ridge</h1>
    <p class="region">MARGARETTE RIVER</p>
    <p class="varietal">Cabernet Merlot</p>
    <p class="side side--left side-heading origin">LOREM IPSUM • AUSTRALIA</p>
    <p class="side side--left side-copy notes-left">Lorem ipsum dolor sit amet, consectetur adipiscing elit. Ut ac dolor ex. Praesent mollis risus nisl, id pretium arcu dignissim non. Curabitur placerat pharetra mi a ullamcorper. Mauris sagittis vehicula odio, non vulputate libero sodales id. Aenean placerat lectus eget faucibus volutpat.</p>
    <p class="side side--right side-heading bottling">BOTTLED ON 08/01/19 • BEST BEFORE 08/01/26</p>
    <p class="side side--right side-copy notes-right">Lorem ipsum dolor sit amet, consectetur adipiscing elit. Ut ac dolor ex. Praesent mollis risus nisl, id pretium arcu dignissim non. Curabitur placerat pharetra mi a ullamcorper. Mauris sagittis vehicula odio, non vulputate libero sodales id. Aenean placerat lectus eget faucibus volutpat.</p>
  </section>

  <section class="label label--bottom">
    <div class="shell-art shell-art--cockle" role="img" aria-label="Engraved illustration of a ribbed cockle seashell in plum ink"></div>
    <span class="est est--word">EST.</span>
    <span class="est est--year">1920</span>
    <h2 class="brand">Tallow Ridge</h2>
    <p class="region">MARGARETTE RIVER</p>
    <p class="varietal">Cabernet Merlot</p>
    <p class="side side--left side-heading origin">LOREM IPSUM • AUSTRALIA</p>
    <p class="side side--left side-copy notes-left">Lorem ipsum dolor sit amet, consectetur adipiscing elit. Ut ac dolor ex. Praesent mollis risus nisl, id pretium arcu dignissim non. Curabitur placerat pharetra mi a ullamcorper. Mauris sagittis vehicula odio, non vulputate libero sodales id. Aenean placerat lectus eget faucibus volutpat.</p>
    <p class="side side--right side-heading bottling">BOTTLED ON 08/01/19 • BEST BEFORE 08/01/26</p>
    <p class="side side--right side-copy notes-right">Lorem ipsum dolor sit amet, consectetur adipiscing elit. Ut ac dolor ex. Praesent mollis risus nisl, id pretium arcu dignissim non. Curabitur placerat pharetra mi a ullamcorper. Mauris sagittis vehicula odio, non vulputate libero sodales id. Aenean placerat lectus eget faucibus volutpat.</p>
  </section>

</main>
</body>
</html>
```